Verpackungsdesign für Kaffeefilter
Sehr gute Kommunikation! Schnelle und zuverlässige Bearbeitung! Klasse, gerne wieder.
Zielgruppe
Wir, TERAL GmbH, sind größter Hersteller von privat label Kaffeefiltern. Für unsere Eigenmarke LIVA Premium Kaffeefilter Größe 4, 80 Stück, braun wird ein kreatives und frisches Verpackungsdesign benötigt. Zielgruppe für die LIVA Premium Kaffeefilter sind internationale Filterkaffeetrinker im Altersspektrum 18 bis 50 Jahre.
Aufgabenstellung
Wir wünschen uns ein Faltschachtel - Design, welches frisch und jugendlich, luxuriös / hochwertig aber nicht opulent/barock, smart und reduziert (nicht überladen), nicht verspielt, abstrakt und schematisch sowie skandinavisch und modern, für einen internationalen Kundenkreis, ist. Die gesamte Faltschachtel (beiliegende Stanze) soll gestaltet werden.
Es sollen weder eine fotografische Filterabbildung noch andere Fotos auf der Verpackung sein.
WPQ Logo und Grüner Falke sowie Herstelleradresse und 3 Barcodefelder werden benötigt.
ACHTUNG: Die Aufreißlasche ist die Rückseite! Die Front steht im Tray. Es wird ca. 25% im unteren Teil der Faltschachtel vom Tray verdeckt.

```html
<!DOCTYPE html>
<html lang="de">
<head>
<meta charset="utf-8">
<title>LIVA Premium Kaffeefilter – Faltschachtel</title>
<link href="https://fonts.googleapis.com/css2?family=Jost:ital,wght@0,400;0,500;0,700;0,800;1,800&display=swap" rel="stylesheet">
<style>
  :root {
    --kraft: #c89c6f;
    --kraft-light: #cfa57a;
    --brown: #6b4420;
    --brown-text: #5e3c1d;
    --yellow: #d3ae0f;
    --ochre: #a9720f;
    --olive: #7d5a18;
    --ink: #1f1a14;
    --cut: #8f7b66;
    --paper: #ffffff;
  }
  html, body { margin: 0; padding: 0; overflow: hidden; }
  body {
    width: 1200px; height: 932px; position: relative;
    background: var(--paper);
    font-family: "Jost", sans-serif; color: var(--ink);
  }
  .panel {
    position: absolute; box-sizing: border-box;
    background: radial-gradient(circle at 30% 20%, var(--kraft-light), var(--kraft) 70%);
    border: 1px solid var(--cut);
  }
  .flap-top    { left: 604px; top: 0;     width: 450px; height: 125px; }
  .panel-back  { left: 0;     top: 125px; width: 455px; height: 677px; }
  .panel-side  { left: 455px; top: 125px; width: 150px; height: 677px; }
  .panel-front { left: 604px; top: 125px; width: 451px; height: 677px; }
  .panel-right { left: 1055px; top: 125px; width: 145px; height: 677px; }
  .flap-bottom { left: 604px; top: 802px; width: 454px; height: 124px; background: var(--paper); }

  .pattern-band {
    position: absolute; left: 458px; top: 272px; width: 742px; height: 216px;
    background: linear-gradient(90deg, var(--yellow), var(--ochre) 20%, var(--olive) 35%, var(--yellow) 50%, var(--brown) 62%, var(--ochre) 78%, var(--yellow) 90%, var(--olive));
  }

  .tear-mark { position: absolute; left: 71px; top: 354px; width: 82px; height: 226px; }

  .rotated { position: absolute; transform: rotate(90deg); transform-origin: center; }
  .howto { width: 490px; height: 160px; left: 110px; top: 360px; }
  .howto h2 { margin: 0 0 8px; font-weight: 400; font-size: 23px; text-align: center; color: var(--ink); }
  .howto p { margin: 0; font-size: 12px; line-height: 15.5px; color: var(--ink); }
  .open-hint { width: 450px; height: 72px; left: -22px; top: 424px;
    font-size: 27px; line-height: 34px; color: var(--ink); }

  .side-copy { position: absolute; left: 479px; width: 120px; font-size: 14.5px; line-height: 17.8px; color: var(--ink); }
  .side-copy.top { top: 146px; }
  .side-copy.bottom { top: 519px; }

  .brand { position: absolute; right: 168px; text-align: right; color: var(--brown); }
  .brand-name { top: 138px; font-weight: 800; font-size: 44px; letter-spacing: 22px; margin-right: -22px; }
  .brand-line { top: 186px; font-weight: 500; font-size: 37px; letter-spacing: 14px; margin-right: -14px; }

  .product { position: absolute; right: 163px; text-align: right; color: var(--brown-text); }
  .product-title { top: 497px; font-weight: 800; font-style: italic; font-size: 31px; letter-spacing: 5px; }
  .product-spec { top: 534px; font-size: 22px; line-height: 29.5px; letter-spacing: 3.5px; font-weight: 400; }

  .cert-seal { position: absolute; left: 864px; top: 648px; width: 46px; height: 46px; border-radius: 50%; background: #1d5fa8; }
  .cert-box { position: absolute; left: 919px; top: 647px; width: 116px; height: 50px; border: 1px solid var(--ink); border-radius: 3px; box-sizing: border-box; }

  .address { position: absolute; left: 1077px; top: 513px; font-size: 14.5px; line-height: 18px; color: var(--ink); }

  .flap-title { position: absolute; left: 786px; top: 18px; color: var(--brown-text); }
  .flap-title .t { font-weight: 800; font-style: italic; font-size: 23px; letter-spacing: 4px; line-height: 30px; }
  .flap-title .s { font-size: 17px; letter-spacing: 3px; line-height: 24px; }
</style>
</head>
<body>
  <div class="panel flap-top"></div>
  <div class="panel panel-back"></div>
  <div class="panel panel-side"></div>
  <div class="panel panel-front"></div>
  <div class="panel panel-right"></div>
  <div class="panel flap-bottom"></div>

  <div class="flap-title">
    <div class="t">KAFFEEFILTER</div>
    <div class="s">GRÖSSE4</div>
    <div class="s">80 STÜCK</div>
  </div>

  <svg class="tear-mark" viewBox="0 0 82 226" aria-hidden="true">
    <rect width="82" height="226" fill="var(--yellow)"/>
    <polygon points="82,0 0,113 82,226" fill="var(--brown)"/>
  </svg>

  <div class="rotated howto">
    <h2>So filtern Sie richtig</h2>
    <p>1. Überprüfen Sie bitte nach dem Umfalten der Doppelnähte, ob Filter und Filterpapier in der Größe übereinstimmen. Dieses Filterpapier Größe 4 passt nur in den Filter Nr. 4.</p>
    <p>2 Pro Tasse etwa einen gehäuften Kaffeelöffel fein gemahlen Kaffee in den Filter geben.</p>
    <p>3. Mit sprudelnd kochendem Wasser das Kaffeemehl anbrühen, dann entsprechend der gewünschten Tassenzahl kochendes Wasser nachgießen.</p>
  </div>

  <div class="rotated open-hint">Hier die Packung an der Stanzlinie öffnen und wieder verschließen</div>

  <div class="side-copy top">Das Filterpapier ist garantiert aus geschmacksneu­tralem, reinem, ungebleichtem Spezialpapier.</div>
  <div class="side-copy bottom">Die Festigkeit der Prägung wird ausschließlich durch hohen Druck ohne Ver­wendung eines Bindemittels er­reicht. Die Kaf­feefilter können mit Inhalt kom­postiert werden.</div>

  <div class="pattern-band" role="img" aria-label="Muster aus flachen Kaffeetassen, Kaffeebohnen und Filtertüten in Gelb- und Brauntönen mit großer Ziffer 4"></div>

  <div class="brand brand-name">LIVA</div>
  <div class="brand brand-line">PREMIUM</div>

  <div class="product product-title">KAFFEEFILTER</div>
  <div class="product product-spec">GRÖSSE4<br>NATURBRAUN - UNGEBLEICHT<br>80 STÜCK</div>

  <div class="cert-seal" aria-hidden="true"></div>
  <div class="cert-box" aria-hidden="true"></div>

  <div class="address">Hersteller und<br>Vertrieb<br>TERAL<br>Filterweg 12<br>54321 Röststadt</div>
</body>
</html>
```